BRAVEN POWERLINE SERVICES needs a vibrant design for electrical contracting work.

I require a card design for my own electrical contracting business. I will be doing a lot of domestic and commercial work, including things such as repairs, maintenance, lighting, installations and various others. LED lighting and energy efficiency will be a big part of my business. I wish not to have childish pictures such as light bulbs in the design, but rather a smart and modern looking card which incorporates my logo colours and perhaps the same lighting strike within the faded background of the card.

Target Market(s)

Residential and Commercial property owners.

Industry/Entity Type

Electrical

Contact Information for Business Card

Dalen Voskic
EC40923
Phone Number: 0417 358 942
Email: dalen@bravenpowerline.com

Font styles to use
Serif
Sans Serif

Requirements
Must have
• My Logo and associated colours.
Nice to have
• Some form of shapes splitting the card into different colours related to the colours of my logo. Electric Blue, Silver/Grey and White.
Should not have
• Childish pictures and symbols such as light bulbs.

```html
<!DOCTYPE html>
<html lang="en">
<head>
<meta charset="utf-8">
<title>Braven Powerline Services – Business Card</title>
<link rel="stylesheet" href="https://fonts.googleapis.com/css2?family=Michroma&family=Lato:wght@400&display=swap">
<style>
  :root {
    --stage: #141517;
    --electric-blue: #1f4fb0;
    --deep-blue: #123a8f;
    --lavender-blue: #7d86c4;
    --brand-navy: #2c2f8c;
    --silver-light: #f4f4f6;
    --silver-mid: #d9dade;
    --white: #ffffff;
    --glow: rgba(190, 215, 255, 0.35);
  }
  * { box-sizing: border-box; margin: 0; padding: 0; }
  html, body {
    width: 1200px; height: 871px; overflow: hidden;
    background: var(--stage);
  }
  .stage {
    width: 1200px; height: 871px;
    display: flex; flex-direction: column; align-items: center; justify-content: center;
    gap: 30px;
  }
  .card {
    position: relative;
    width: 660px; height: 377px;
    overflow: hidden;
  }

  /* Back side */
  .card--back {
    background: linear-gradient(160deg, var(--white) 0%, var(--silver-light) 55%, var(--silver-mid) 100%);
  }
  .card--back .brand {
    position: absolute; left: 0; right: 0; top: 120px;
    display: flex; align-items: center; justify-content: center; gap: 18px;
  }
  .brand-dot {
    width: 46px; height: 46px; border-radius: 50%;
    border: 5px solid var(--brand-navy);
    flex: none;
  }
  .card--back .brand-name {
    font-family: "Michroma", sans-serif;
    font-size: 25px; letter-spacing: 2px;
    color: var(--brand-navy);
    line-height: 1.2;
  }
  .back-rule {
    position: absolute; left: 0; right: 0; top: 268px;
    height: 6px; background: var(--brand-navy);
  }

  /* Front side */
  .card--front {
    background: linear-gradient(100deg, var(--lavender-blue) 0%, var(--electric-blue) 55%, var(--deep-blue) 100%);
    color: var(--white);
  }
  .light-trails {
    position: absolute; inset: 0;
    background:
      radial-gradient(ellipse 45% 35% at 38% 52%, var(--glow), transparent 70%),
      radial-gradient(ellipse 30% 25% at 82% 62%, rgba(255, 220, 240, 0.25), transparent 70%);
  }
  .front-layout {
    position: absolute; inset: 0;
    display: flex; align-items: center;
    padding: 0 40px 0 44px;
  }
  .card--front .brand {
    display: flex; align-items: center; gap: 12px;
    width: 300px;
  }
  .card--front .brand-dot { width: 34px; height: 34px; border: 4px solid var(--white); }
  .card--front .brand-name {
    font-family: "Michroma", sans-serif;
    font-size: 17px; letter-spacing: 1.5px; line-height: 1.35;
    color: var(--white);
  }
  .divider {
    width: 2px; height: 150px; background: var(--white);
    margin: 0 26px 0 10px; flex: none;
  }
  .contact { display: flex; flex-direction: column; gap: 6px; }
  .contact-name {
    font-family: "Michroma", sans-serif;
    font-size: 17px; letter-spacing: 4px; text-transform: uppercase;
  }
  .contact-licence {
    font-family: "Michroma", sans-serif;
    font-size: 14px; letter-spacing: 4px; margin-bottom: 6px;
  }
  .contact-line {
    font-family: "Lato", sans-serif;
    font-size: 16px; display: flex; align-items: center; gap: 8px;
  }
  .contact-line svg { width: 14px; height: 14px; flex: none; }
</style>
</head>
<body>
<main class="stage">

  <section class="card card--back" aria-label="Business card back">
    <div class="brand">
      <span class="brand-dot"></span>
      <span class="brand-name">BRAVEN POWERLINE<br>SERVICES</span>
    </div>
    <div class="back-rule"></div>
  </section>

  <section class="card card--front" aria-label="Business card front">
    <div class="light-trails" role="img" aria-label="Faded swirling light trails across a blue background"></div>
    <div class="front-layout">
      <div class="brand">
        <span class="brand-dot"></span>
        <span class="brand-name">BRAVEN POWERLINE<br>SERVICES</span>
      </div>
      <div class="divider"></div>
      <div class="contact">
        <p class="contact-name">Dalen Voskic</p>
        <p class="contact-licence">EC40923</p>
        <p class="contact-line">
          <svg viewBox="0 0 16 16" aria-hidden="true"><path fill="#fff" d="M3 2h3l1.5 3.5-2 1.3a9 9 0 0 0 3.7 3.7l1.3-2L14 10v3a1 1 0 0 1-1 1A12 12 0 0 1 2 3a1 1 0 0 1 1-1z"/></svg>
          0417 358 942
        </p>
        <p class="contact-line">
          <svg viewBox="0 0 16 16" aria-hidden="true"><rect x="1" y="3" width="14" height="10" fill="none" stroke="#fff" stroke-width="1.5"/><path d="M1 3l7 6 7-6" fill="none" stroke="#fff" stroke-width="1.5"/></svg>
          dalen@bravenpowerline.com
        </p>
      </div>
    </div>
  </section>

</main>
</body>
</html>
```